Upbeat Accouting Package Flyer

I am looking for a 1 page (front, or front and back) flyer that will become our marketing for our accounting services. We are looking for something a little different and we are catering to the small retail shop owners. We have 3 accounting packages we would like to display and then some add-ons. I have included our logo that must be included in the design. I have uploaded the accounting package information as well.
Target Market(s)
Small Retail Shop Owners
Industry/Entity Type
Accounting
Colors
Designer to choose colors to be used in the design.
Requirements
Must have
- A casual feel. We are not your typical accountants who are very professional and "stuffy". I want it to feel like we are all family.
Nice to have
- I would like to incorporate some sort of retail theme.
- We have a couple of taglines we like to use and it would be great if they could be included. They are "We know you CAN do the accounting, but do you WANT to?" and "We allow you to get back to what's important."
Should not have
- Typical stock accounting photos of people shaking hands, large office buildings, etc.

```html
<!DOCTYPE html>
<html lang="en">
<head>
<meta charset="utf-8">
<title>Brightwell Tax &amp; Accounting – Packages</title>
<link href="https://fonts.googleapis.com/css2?family=Oswald:wght@500;600&family=Pathway+Gothic+One&display=swap" rel="stylesheet">
<style>
  :root {
    --teal: #4ff7df;
    --teal-soft: #a8f5ee;
    --ink: #262b2e;
    --paper: #ffffff;
    --photo-dark: #2a3430;
    --photo-mid: #7d8f86;
    --photo-light: #c9d3cc;
  }
  html, body { margin: 0; padding: 0; overflow: hidden; }
  body { background: var(--paper); }
  .flyer {
    position: relative;
    width: 846px;
    height: 1200px;
    overflow: hidden;
    background: var(--paper);
    color: var(--ink);
    font-family: "Pathway Gothic One", "Arial Narrow", sans-serif;
  }
  .brand {
    position: absolute;
    left: 34px;
    top: 44px;
    margin: 0;
    font-family: "Oswald", sans-serif;
    font-weight: 500;
    font-size: 40px;
    line-height: 1;
    letter-spacing: 0.5px;
    color: var(--ink);
  }
  .corner-accent, .footer-accent { position: absolute; left: 0; top: 0; }
  .hero {
    position: absolute;
    left: 0;
    top: 140px;
    width: 846px;
    height: 562px;
    background:
      radial-gradient(ellipse at 45% 40%, var(--photo-light) 0%, transparent 45%),
      radial-gradient(ellipse at 70% 75%, var(--photo-mid) 0%, transparent 55%),
      linear-gradient(160deg, var(--photo-dark) 0%, var(--photo-mid) 45%, #5d6d65 75%, var(--photo-dark) 100%);
  }
  .package {
    position: absolute;
    width: 380px;
  }
  .package h2 {
    position: relative;
    display: inline-block;
    margin: 0 0 4px;
    padding: 2px 14px 2px 0;
    font-family: "Oswald", sans-serif;
    font-weight: 600;
    font-size: 19px;
    line-height: 24px;
    color: var(--ink);
    z-index: 0;
  }
  .package h2::before {
    content: "";
    position: absolute;
    left: -12px;
    right: -2px;
    top: 1px;
    bottom: 1px;
    background: var(--teal-soft);
    border-radius: 16px;
    z-index: -1;
  }
  .package ul {
    list-style: none;
    margin: 0;
    padding: 0;
    font-size: 16.5px;
    line-height: 24.2px;
  }
  .develop { left: 59px; top: 712px; }
  .relax   { left: 59px; top: 896px; }
  .grow    { left: 414px; top: 712px; }
  .extras  { left: 414px; top: 992px; }
  .extras ul { font-size: 18px; line-height: 26.4px; }
</style>
</head>
<body>
<main class="flyer">
  <h1 class="brand">Brightwell Tax &amp; Accounting</h1>

  <svg class="corner-accent" width="846" height="170" aria-hidden="true">
    <polygon points="640,166 688,110 846,110 846,166" fill="var(--teal)"/>
  </svg>

  <div class="hero" role="img" aria-label="Close-up photograph of crumpled dollar bills with a few coins resting on top"></div>

  <section class="package develop">
    <h2>Develop:</h2>
    <ul>
      <li>$300/mo when paid annually $325/mo billed monthly</li>
      <li>CloudLedger Online subscription</li>
      <li>Free accounting setup</li>
      <li>Weekly transaction processing</li>
      <li>Monthly account reconciliation (up to 2 accounts)</li>
      <li>Monthly financial statements by the 15th of the month</li>
    </ul>
  </section>

  <section class="package relax">
    <h2>Relax (We’ve Got This):</h2>
    <ul>
      <li>$850/mo billed annually; $875/mo billed monthly</li>
      <li>CloudLedger Online subscription</li>
      <li>Free accounting setup</li>
      <li>Weekly transaction processing</li>
      <li>Monthly account reconciliation (up to 5-10 accounts)</li>
      <li>Monthly financial statements by the 5th of the month</li>
      <li>Client portal access for document sharing</li>
      <li>2 Custom Reports</li>
      <li>Accounts Payable</li>
      <li>Invoicing and accounts receivable</li>
      <li>Weekly Scorecard (customized metric tracking for your business)</li>
    </ul>
  </section>

  <section class="package grow">
    <h2>Grow:</h2>
    <ul>
      <li>$550/mo billed annually; $575/mo billed monthly</li>
      <li>CloudLedger Online subscription</li>
      <li>Free accounting setup</li>
      <li>Weekly transaction processing</li>
      <li>Monthly account reconciliation (up to 4 accounts)</li>
      <li>Monthly financial statements by the 10th of the month</li>
      <li>Client portal access for document sharing</li>
      <li>1 Custom Report</li>
      <li>Accounts Payable</li>
      <li>Monthly Scorecard (customized metric tracking for your business)</li>
    </ul>
  </section>

  <svg class="footer-accent" width="846" height="1200" aria-hidden="true">
    <polygon points="576,1064 846,1064 846,1192 524,1192" fill="var(--teal)"/>
    <rect x="0" y="1192" width="846" height="8" fill="var(--teal)"/>
  </svg>

  <section class="package extras">
    <h2>Additional Options</h2>
    <ul>
      <li>Payroll – 1-10 employees $85/mo; 11-30 employees $175/mo</li>
      <li>Sales tax - $30/mo per state</li>
      <li>Corporate taxes $50/mo</li>
      <li>Owner taxes - $25/mo</li>
    </ul>
  </section>
</main>
</body>
</html>
```